Very new and innovative Web design for Property managers of Vacation rentals

We are looking for a new website design for travel agencies and property managers specialised on vacation rentals business, holiday villas and apartments.

The end users of this website are travellers who are looking for a vacation home for their next holiday: this is the reason why the website must be easy to use, attractive, professional, possibly elegant and focused on get new reservations.

This is a draft of our current website: https://demo5.holdiquay.com/
Please consider that we would like to have proposals with a totally different and innovative layout, surprise us!

These are the pages of the website:
• Homepage: feel free to redesign all the homepage as you wish, surprise us with something very new! Please consider that Property manager/Travel agencies usually want to have the opportunity to put in evidence groups of houses with specific characteristics (eg. villas with private swimming pool, apartment in big/small towns, villas with air co, etc…), destinations and tourist areas, and sometimes experiences or activities (please consider that the website layout must be suitable even if some of the previous sections are not used).
• Search page: we’d like to organise the results of the search page in three different ways:
o Grid
o Map
o List
• Property page: to illustrate the characteristics, descriptions, images, …. of the property. It is very important to put in evidence images of the property and to maintain the booking form (and the other call to action bottom – eg. whatsapp) always visible
• Custom pages: static pages composed usually by text, images and call to actions
• Contact us (general form)
• Info request (specific of a property form)
• Booking process
• Blog, organised in four pages:
o Home Page – introduction to the blog
o List of articles
o Single article
o Site Map (presentation of categories and sub-categories)

If possible, we’d prefer to receive the material in Adobe XD or similar so that we can obtain the three versions:
- smartphone
- tablet
- desktop

The website will be then developed in Bootstrap: as a result we’ll need the icons in SVG format (or the library used)

In attachment you can find the map of the website pages

```html
<!DOCTYPE html>
<html lang="en">
<head>
<meta charset="utf-8">
<title>Holdiquay – Vacation Rentals</title>
<link href="https://fonts.googleapis.com/css2?family=Questrial&family=Montserrat:wght@400;500;600;700&family=Oswald:wght@400;500&family=Great+Vibes&display=swap" rel="stylesheet">
<style>
:root{
  --green:#1fb98a;
  --green-dark:#17a078;
  --orange:#f58a4b;
  --teal:#29495a;
  --navy:#0f2834;
  --navy-2:#123240;
  --ink:#222a2f;
  --muted:#5d666b;
  --white:#ffffff;
}
*{margin:0;padding:0;box-sizing:border-box}
html,body{width:1200px;height:3950px;overflow:hidden;background:#fff}
body{font-family:"Montserrat",sans-serif;color:var(--ink)}
.page{position:relative;width:1200px;height:3950px;overflow:hidden}
.abs{position:absolute}
.photo{position:absolute}
a{color:inherit;text-decoration:none}

/* header */
.logo{position:absolute;display:flex;align-items:center;gap:8px;font-family:"Questrial",sans-serif;font-size:27px;color:var(--ink)}
.logo .dot{width:30px;height:30px;border-radius:50%;background:var(--green)}
.callus{position:absolute;left:838px;top:21px;font-family:"Oswald",sans-serif;font-size:13px;color:var(--ink)}
.callus b{color:var(--green);font-weight:500}
.social{position:absolute;width:24px;height:24px;border-radius:50%;border:1.5px solid var(--green)}
.nav{position:absolute;top:58px;font-size:11px;font-weight:600;color:var(--ink)}
.nav.active{color:var(--green)}
.btn{position:absolute;display:flex;align-items:center;justify-content:center;border-radius:14px;color:#fff;font-size:10.5px;font-weight:600}
.btn.green{background:var(--green)}
.btn.orange{background:var(--orange)}

/* hero */
.hero-photo{left:0;top:95px;width:1200px;height:560px;background:linear-gradient(180deg,#9db8cf 0%,#c7d3dc 35%,#b5a48e 62%,#5b6d73 85%,#3f5561 100%)}
.tag{position:absolute;left:199px;top:211px;width:181px;height:21px;background:var(--green);color:#fff;font-family:"Oswald",sans-serif;font-size:13px;padding:2px 12px}
.hero-h{position:absolute;left:199px;font-family:"Oswald",sans-serif;font-size:33px;font-weight:500;color:#111;letter-spacing:.5px}
.script{font-family:"Great Vibes",cursive;font-weight:400}
.hero-p{position:absolute;left:199px;top:340px;width:290px;font-size:11px;line-height:16px;color:#111}
.field{position:absolute;top:679px;height:37px;width:156px;background:#fff;border-radius:19px;font-size:9px;color:#888;display:flex;align-items:center;padding-left:26px;gap:10px}
.field .ico{width:9px;height:9px;border:1.5px solid #999;border-radius:2px}
.field .chev{position:absolute;right:20px;top:14px;width:6px;height:6px;border-right:1.5px solid #888;border-bottom:1.5px solid #888;transform:rotate(45deg)}

/* sections */
.title{position:absolute;left:313px;font-family:"Questrial",sans-serif;font-size:23px;letter-spacing:.5px;color:var(--ink)}
.title.light{color:#fff}
.rule{position:absolute;left:293px;width:121px;height:1px;background:#777}
.lead{position:absolute;left:432px;width:450px;font-size:10.5px;line-height:15px;color:var(--muted)}
.lead.light{color:#d8e2e6}
.rule.light{background:#9fb1b8}
.amen{position:absolute;top:945px;width:120px}
.amen svg{display:block;height:34px}
.amen h4{margin-top:16px;font-size:12.5px;font-weight:600;color:var(--ink)}
.amen p{margin-top:6px;font-size:9.5px;line-height:14px;color:var(--muted)}

.act{position:absolute;top:1497px;width:181px;height:180px;box-shadow:0 8px 16px rgba(0,0,0,.15)}
.act .lbl{position:absolute;left:0;bottom:0;width:150px;height:26px;background:var(--green);color:#fff;font-size:12px;font-weight:600;padding:6px 12px;border-top-right-radius:26px}

.tile-label{position:absolute;color:#fff;font-size:14px;font-weight:600;letter-spacing:.5px}

.vcard-img{position:absolute;top:2687px;width:277px;height:133px}
.stars{position:absolute;top:0;left:0;width:66px;height:16px;background:var(--orange);color:#fff;font-size:10px;padding-left:5px;letter-spacing:1px;line-height:16px}
.vname{position:absolute;top:2834px;font-size:13.5px;font-weight:600;color:#fff}
.vdesc{position:absolute;top:2866px;width:275px;font-size:9.5px;line-height:14px;color:#d0dade}
.stat{position:absolute;font-size:10px;color:#e6edf0;display:flex}
.stat span{display:inline-block;width:80px;color:var(--green);padding-left:20px;position:relative}
.stat span::before{content:"";position:absolute;left:0;top:2px;width:12px;height:9px;border:1.5px solid var(--green);border-radius:2px}
.arrow-c{position:absolute;top:2751px;width:24px;height:24px;border-radius:50%;border:1.5px solid var(--green)}

.art-img{position:absolute;top:3257px;width:250px;height:161px}
.art{position:absolute;top:3383px;width:208px;height:173px;background:#fff;padding:16px 16px}
.art .date{font-family:"Oswald",sans-serif;font-size:9.5px;color:var(--ink)}
.art .date i{display:inline-block;width:8px;height:8px;border:1.5px solid var(--green);border-radius:2px;margin-right:6px;vertical-align:-1px}
.art .date i.c{border-radius:50%;margin-left:12px}
.art h5{margin-top:9px;font-size:11.5px;line-height:14px;font-weight:600}
.art p{margin-top:12px;font-size:9px;line-height:14px;color:var(--muted)}

.foot-h{position:absolute;top:3714px;font-size:12px;font-weight:600;color:#fff}
.foot-t{position:absolute;font-size:10px;line-height:18.4px;color:#e2eaee}
</style>
</head>
<body>
<div class="page">

<!-- Header -->
<header>
  <div class="logo" style="left:107px;top:30px"><span class="dot"></span>Holdiquay</div>
  <div class="callus"><b>CALL US:</b> &#9742; +39 055 0100200</div>
  <span class="social" style="left:1007px;top:17px"></span>
  <span class="social" style="left:1039px;top:17px"></span>
  <span class="social" style="left:1070px;top:17px"></span>
  <nav>
    <a class="nav active" style="left:527px">-- Home --</a>
    <a class="nav" style="left:607px">About Us</a>
    <a class="nav" style="left:679px">Special Offers</a>
    <a class="nav" style="left:779px">Experience</a>
    <a class="nav" style="left:862px">Blog</a>
    <a class="nav" style="left:910px">Contact Us</a>
    <a class="btn green" style="left:993px;top:53px;width:100px;height:24px">Book Now!</a>
  </nav>
</header>

<!-- Hero -->
<section>
  <div class="photo hero-photo" role="img" aria-label="Venice canal with gondolas and a domed basilica under a cloudy sky"></div>
  <svg class="abs" style="left:0;top:520px" width="1200" height="260" viewBox="0 0 1200 260">
    <path d="M0 30 C150 20 260 90 480 70 C700 48 850 20 1000 28 C1100 34 1160 45 1200 40 L1200 260 L0 260Z" fill="#1fb98a"/>
  </svg>
  <div class="tag">SUMMER 2021</div>
  <div class="hero-h" style="top:250px">TAKE <span class="script" style="color:var(--orange);font-size:56px;line-height:0;vertical-align:-4px">Your</span> HOLIDAY</div>
  <div class="hero-h" style="top:292px">TO THE NEXT LEVEL</div>
  <p class="hero-p">Lorem Ipsum is simply dummy text of the printing and typesetting orem Ipsum has been</p>
  <a class="btn orange" style="left:199px;top:392px;width:100px;height:23px">Book Now!</a>
  <div class="abs script" style="left:450px;top:552px;font-size:34px;color:#fff">Exclusive Villas in Italy</div>
  <svg class="abs" style="left:581px;top:601px" width="36" height="36"><circle cx="18" cy="18" r="17" fill="#8fd3bb"/><path d="M12 15l6 6 6-6" stroke="#fff" stroke-width="2" fill="none"/></svg>
  <div class="field" style="left:199px"><span class="ico"></span>Destination<span class="chev"></span></div>
  <div class="field" style="left:368px"><span class="ico"></span>Check In<span class="chev"></span></div>
  <div class="field" style="left:536px"><span class="ico"></span>Check Out<span class="chev"></span></div>
  <div class="field" style="left:705px"><span class="ico" style="border-radius:50%"></span>Travelers<span class="chev"></span></div>
  <a class="btn orange script" style="left:874px;top:679px;width:125px;height:37px;border-radius:19px;font-size:22px;font-weight:400">Search</a>
</section>

<!-- Amenities -->
<section>
  <h2 class="title" style="top:834px">Exquisite Amenities</h2>
  <div class="rule" style="top:886px"></div>
  <p class="lead" style="top:880px">Lorem ipsum dolor sit amet, consectetur adipiscing elit, sed do eiusmod tempor incididunt ut labore et dolore magna aliqua.</p>

  <div class="amen" style="left:313px">
    <svg width="40" height="34" viewBox="0 0 40 34" fill="none" stroke="#1fb98a" stroke-width="2"><path d="M3 12a24 24 0 0 1 34 0M8 17a17 17 0 0 1 24 0M13 22a10 10 0 0 1 14 0"/><circle cx="20" cy="28" r="2.5" fill="#1fb98a"/></svg>
    <h4>Free WiFi</h4><p>incididunt ut voluptatem site dolore</p>
  </div>
  <div class="amen" style="left:461px">
    <svg width="40" height="34" viewBox="0 0 40 34" fill="none" stroke="#1fb98a" stroke-width="2"><circle cx="26" cy="9" r="7"/><path d="M4 28v-7l4-7h14l4 7v7zM4 28h22"/><circle cx="10" cy="28" r="3"/><circle cx="20" cy="28" r="3"/></svg>
    <h4>Free car parking</h4><p>incididunt ut voluptatem site dolore</p>
  </div>
  <div class="amen" style="left:610px">
    <svg width="40" height="34" viewBox="0 0 40 34" fill="none" stroke="#1fb98a" stroke-width="2"><path d="M8 22V6a4 4 0 0 1 8 0M20 22V6a4 4 0 0 1 8 0M8 12h12M8 18h12M2 26c4-3 6 3 10 0s6 3 10 0 6 3 10 0M2 32c4-3 6 3 10 0s6 3 10 0 6 3 10 0"/></svg>
    <h4>Swimming pool</h4><p>incididunt ut labore than site dolore</p>
  </div>
  <div class="amen" style="left:760px">
    <svg width="40" height="34" viewBox="0 0 40 34" fill="none" stroke="#1fb98a" stroke-width="2"><rect x="3" y="5" width="34" height="16" rx="2"/><path d="M8 16h24M10 26l-2 5M18 26l-2 5M26 26l-2 5"/></svg>
    <h4>Air conditioner</h4><p>incididunt ut labore than site dolore</p>
  </div>

  <a class="btn orange" style="left:313px;top:1070px;width:101px;height:26px">Book Now!</a>
</section>

<!-- Other activities band -->
<section>
  <div class="abs" style="left:0;top:1288px;width:1200px;height:300px;background:var(--teal)"></div>
  <div class="photo" style="left:313px;top:1143px;width:397px;height:189px;background:linear-gradient(180deg,#6aa8d8 0%,#cfd6d0 45%,#9d8b6a 65%,#2aa7b4 100%)" role="img" aria-label="Clifftop town above turquoise sea"></div>
  <div class="photo" style="left:650px;top:1070px;width:237px;height:222px;background:linear-gradient(180deg,#f6c55f 0%,#e48c3c 45%,#8b5a35 75%,#4b3a2c 100%);border:5px solid #fff;border-top:none" role="img" aria-label="Ancient amphitheatre at sunset"></div>

  <h2 class="title light" style="top:1388px">Other Activities</h2>
  <div class="rule light" style="top:1441px"></div>
  <p class="lead light" style="top:1434px">Lorem ipsum dolor sit amet, consectetur adipiscing elit, sed do eiusmod tempor incididunt ut labore et dolore magna aliqua.</p>

  <div class="act" style="left:199px"><div class="photo" style="inset:0;background:linear-gradient(180deg,#7d9bb8,#c6854a 55%,#4e5b48)" role="img" aria-label="Hikers on a mountain trail"></div><div class="lbl">Hiking Vacations</div></div>
  <div class="act" style="left:406px"><div class="photo" style="inset:0;background:linear-gradient(180deg,#e9f2f4,#7fc8d8 55%,#1b8ea8)" role="img" aria-label="Surfer riding a wave"></div><div class="lbl">Surf Destinations</div></div>
  <div class="act" style="left:612px"><div class="photo" style="inset:0;background:linear-gradient(180deg,#a8c9dc,#4c8ea6 55%,#2b6878)" role="img" aria-label="Whale tail above the sea"></div><div class="lbl">Whale Watching</div></div>
  <div class="act" style="left:818px"><div class="photo" style="inset:0;background:linear-gradient(180deg,#3f7fc6,#8fb9e4 60%,#cfe0ef)" role="img" aria-label="Tandem skydivers in the sky"></div><div class="lbl">Skydiving</div></div>
</section>

<!-- Exclusive holiday -->
<section>
  <h2 class="title" style="top:1734px">Looking for an Exclusive Holiday?</h2>
  <div class="rule" style="top:1787px"></div>
  <p class="lead" style="top:1780px;width:450px">Browse our vacation rental selections If you are looking for a real experiences, our portal is the right solution. Our vacation homes are all located in Italy and we take care of them and their owners at every time. Our goal is give to our guest authentic taste of holiday and our country.</p>

  <div class="photo" style="left:313px;top:1868px;width:297px;height:327px;background:linear-gradient(180deg,#6f6f98,#9a8aa0 40%,#5d4b46 75%,#3a3236)" role="img" aria-label="Modern luxury villa at dusk"></div>
  <div class="tile-label" style="left:343px;top:2145px">Luxury Villas</div>

  <div class="photo" style="left:313px;top:2195px;width:297px;height:323px;background:linear-gradient(180deg,#c9cdd2,#9a8f84 50%,#5b5048)" role="img" aria-label="Couple of travellers reading a map in a city square"></div>
  <div class="tile-label" style="left:343px;top:2470px">Browse All Vacation Rentals</div>

  <div class="photo" style="left:610px;top:2155px;width:277px;height:250px;background:linear-gradient(180deg,#5fa7d6,#8cc5e8 60%,#9ba6ad 85%,#7a858c)" role="img" aria-label="Woman in a sun hat relaxing in a swimming pool"></div>
  <div class="tile-label" style="left:640px;top:2359px">Last Minute Deals</div>

  <div class="abs" style="left:592px;top:1907px;width:295px;height:248px;background:linear-gradient(160deg,#2dc08f,#1fa97f)"></div>
  <div class="tile-label" style="left:621px;top:2046px">Experiences</div>
  <div class="abs" style="left:622px;top:2081px;width:200px;font-size:11px;line-height:15px;color:#fff;font-weight:600;text-decoration:underline">Don't live just a holiday but an experience! Let's discover our services</div>

  <a class="btn green" style="left:705px;top:2449px;width:87px;height:25px">Read More</a>
</section>

<!-- New villas -->
<section>
  <div class="abs" style="left:0;top:2518px;width:1200px;height:580px;background:var(--navy)"></div>
  <h2 class="title light" style="top:2583px">New Villas and Vacation Rentals</h2>
  <div class="rule light" style="top:2636px"></div>
  <p class="lead light" style="top:2629px">Lorem ipsum dolor sit amet, consectetur adipiscing elit, sed do eiusmod tempor incididunt ut labore et dolore magna aliqua.</p>

  <div class="vcard-img" style="left:313px"><div class="photo" style="inset:0;background:linear-gradient(180deg,#8fb0c2,#5f8a4c 55%,#3fb0c4)" role="img" aria-label="Country villa garden with pool and parasols"></div><div class="stars">★★★★★</div></div>
  <div class="vcard-img" style="left:610px"><div class="photo" style="inset:0;background:linear-gradient(180deg,#5e98cf,#dfe3e5 50%,#2f8fc2)" role="img" aria-label="Modern white villa with infinity pool"></div><div class="stars">★★★★★</div></div>
  <span class="arrow-c" style="left:298px"></span>
  <span class="arrow-c" style="left:877px"></span>

  <div class="vname" style="left:313px">Podere Le Querce</div>
  <p class="vdesc" style="left:313px">The owners offer a wide choice of Extra Services to make you feel welcome and to help you discover Tus­cany in a "non touristy" way.</p>
  <div class="stat" style="left:313px;top:2925px"><span>Sleeps:</span>27</div>
  <div class="stat" style="left:313px;top:2943px"><span>Bedrooms:</span>10</div>
  <div class="stat" style="left:313px;top:2961px"><span>Bathrooms:</span>06</div>
  <div class="stat" style="left:313px;top:2980px"><span>Price:</span>€ 3400 per week</div>
  <a class="btn green" style="left:313px;top:3010px;width:73px;height:23px">More Info</a>
  <a class="btn orange" style="left:395px;top:3010px;width:97px;height:23px">Book Now!</a>

  <div class="vname" style="left:610px">Agriturismo La Collina</div>
  <p class="vdesc" style="left:610px">Il casale è immerso nella campagna toscana ma a soli 3 km dal paese più vicino dove potete trovare tutti i negozi con le principali comodità.</p>
  <div class="stat" style="left:610px;top:2925px"><span>Sleeps:</span>07</div>
  <div class="stat" style="left:610px;top:2943px"><span>Bedrooms:</span>02</div>
  <div class="stat" style="left:610px;top:2961px"><span>Bathrooms:</span>02</div>
  <div class="stat" style="left:610px;top:2980px"><span>Price:</span>€ 3400 per week</div>
  <a class="btn green" style="left:610px;top:3010px;width:73px;height:23px">More Info</a>
  <a class="btn orange" style="left:692px;top:3010px;width:97px;height:23px">Book Now!</a>
</section>

<!-- Articles -->
<section>
  <h2 class="title" style="top:3153px">Latest Articles</h2>
  <div class="rule" style="top:3207px"></div>
  <p class="lead" style="top:3200px">Lorem ipsum dolor sit amet, consectetur adipiscing elit, sed do eiusmod tempor incididunt ut labore et dolore magna aliqua.</p>

  <div class="art-img photo" style="left:199px;background:linear-gradient(180deg,#3f5a2c,#d97a3c 45%,#2f4a24)" role="img" aria-label="Orange lily in a garden"></div>
  <div class="art-img photo" style="left:475px;background:linear-gradient(180deg,#3b5a30,#e8e6de 50%,#4d6b36)" role="img" aria-label="White garden gazebo on a lawn"></div>
  <div class="art-img photo" style="left:749px;background:linear-gradient(180deg,#86aed4,#3f6c3a 55%,#6c8b3f)" role="img" aria-label="Garden with trees and flower beds"></div>

  <article class="art" style="left:220px"><div class="date"><i></i>MARCH-20-2021 <i class="c"></i>1:00PM - 7:00PM</div><h5>Contrary to popular belief, is lorem Ipsum is simply</h5><p>It is a long established fact that a reader will be distracted by the read­able content of a page ...</p><a class="btn green" style="left:18px;top:136px;width:76px;height:22px;font-size:9.5px">Read More</a></article>
  <article class="art" style="left:496px"><div class="date"><i></i>MARCH-20-2021 <i class="c"></i>1:00PM - 7:00PM</div><h5>Contrary to popular belief, is lorem Ipsum is simply</h5><p>It is a long established fact that a reader will be distracted by the read­able content of a page ...</p><a class="btn green" style="left:18px;top:136px;width:76px;height:22px;font-size:9.5px">Read More</a></article>
  <article class="art" style="left:770px"><div class="date"><i></i>MARCH-20-2021 <i class="c"></i>1:00PM - 7:00PM</div><h5>Contrary to popular belief, is lorem Ipsum is simply</h5><p>It is a long established fact that a reader will be distracted by the read­able content of a page ...</p><a class="btn green" style="left:18px;top:136px;width:76px;height:22px;font-size:9.5px">Read More</a></article>
</section>

<!-- Footer -->
<footer>
  <svg class="abs" style="left:0;top:3590px" width="1200" height="360" viewBox="0 0 1200 360">
    <path d="M0 18 C200 -6 420 40 640 26 C860 12 1020 2 1200 10 L1200 360 L0 360Z" fill="#1fb98a"/>
    <path d="M0 56 C260 40 460 52 700 36 C900 22 1060 30 1200 22 L1200 360 L0 360Z" fill="#10303d"/>
  </svg>

  <div class="foot-h" style="left:199px">Contact Us</div>
  <div class="abs" style="left:199px;top:3739px;font-size:18px;color:var(--green)">Call: +39 055 0100200</div>
  <div class="foot-t" style="left:199px;top:3761px;text-decoration:underline">info@holdiquay.com</div>
  <div class="foot-t" style="left:199px;top:3793px;line-height:16px;width:200px">Address:<br>via delle Rose 12, 52100 Borgo Verde, Arezzo (Italy)</div>

  <div class="foot-h" style="left:475px">Quick Links</div>
  <div class="foot-t" style="left:475px;top:3738px">Home<br>About Us<br>Special Offers<br>Experience<br>Blog<br>Contact Us</div>
  <div class="foot-t" style="left:566px;top:3738px">Login<br>Register<br>Wish List<br>Privacy policy<br>Terms &amp; conditions</div>

  <div class="foot-h" style="left:749px">Sign Up Newsletter</div>
  <div class="foot-t" style="left:749px;top:3755px;line-height:14px;width:190px">Lorem ipsum dolor sit amet, sedtur consectetur adipiscing</div>
  <div class="abs" style="left:749px;top:3780px;width:250px;height:29px;border-radius:15px;background:#1f4350;color:#c9d5da;font-size:9.5px;padding:8px 16px">Enter your email ...</div>
  <svg class="abs" style="left:971px;top:3783px" width="24" height="24"><circle cx="12" cy="12" r="11" fill="#f58a4b"/><path d="M7 12h9M12 8l4 4-4 4" stroke="#fff" stroke-width="1.8" fill="none"/></svg>

  <div class="abs" style="left:0;top:3893px;width:1200px;height:57px;background:#224656"></div>
  <div class="logo" style="left:199px;top:3905px;color:#fff;font-size:25px"><span class="dot" style="width:26px;height:26px"></span>Holdiquay</div>
  <div class="abs" style="left:475px;top:3916px;font-size:9.5px;color:#e2eaee">© 2021 <span style="color:var(--green)">Holdiquay</span>. All Rights Reserved</div>
  <span class="social" style="left:750px;top:3910px"></span>
  <span class="social" style="left:780px;top:3910px;background:var(--green)"></span>
  <span class="social" style="left:811px;top:3910px"></span>
  <svg class="abs" style="left:1083px;top:3908px" width="22" height="24"><path d="M3 22L11 3l8 19M7 14h8" stroke="#1fb98a" stroke-width="2" fill="none"/></svg>
</footer>

</div>
</body>
</html>
```